Trade Show Display

We need a design for a trade show pop up display. It should incorporate our colors and logo and should complement our other advertising pieces. Our primary brochure is uploaded. Also uploaded is a file with the text to be included and another file with the display dimensions.

```html
<!DOCTYPE html>
<html lang="en">
<head>
<meta charset="utf-8">
<title>Workforce Anchor Partners – Trade Show Display</title>
<link href="https://fonts.googleapis.com/css2?family=Oswald:wght@500&family=Quicksand:wght@500&display=swap" rel="stylesheet">
<style>
  :root {
    --navy: #0d3a5c;
    --navy-deep: #0a2f4c;
    --green: #8cae3d;
    --ring: #6f8fae;
    --paper: #f7f8f9;
    --stage: #ffffff;
    --white: #ffffff;
  }
  * { margin: 0; padding: 0; box-sizing: border-box; }
  html, body { width: 788px; height: 1200px; overflow: hidden; background: var(--stage); }
  .display {
    position: absolute; left: 0; top: 336px;
    width: 788px; height: 527px;
    background: var(--paper);
    overflow: hidden;
    box-shadow: 0 2px 6px rgba(0,0,0,.18);
  }
  .photo-area {
    position: absolute; left: 300px; top: 0; width: 488px; height: 527px;
    background: linear-gradient(90deg, rgba(247,248,249,1) 0%, rgba(215,224,234,.55) 40%, rgba(170,190,212,.7) 75%, rgba(150,172,198,.75) 100%);
  }
  .brand {
    position: absolute; left: 200px; top: 62px;
    display: flex; align-items: center; gap: 12px;
  }
  .brand-dot { width: 40px; height: 40px; border-radius: 50%; background: var(--navy); }
  .brand-name {
    font-family: "Quicksand", sans-serif; font-weight: 500;
    font-size: 24px; letter-spacing: .5px; color: var(--navy);
    line-height: 1.1; width: 330px;
  }
  .headline {
    position: absolute; left: 113px; top: 120px; width: 562px; height: 48px;
    background: var(--navy); border-radius: 24px;
    font-family: "Quicksand", sans-serif; font-weight: 500;
    font-size: 34px; line-height: 48px; color: var(--white);
    text-align: center;
  }
  .service {
    position: absolute; display: flex; align-items: flex-start; gap: 10px;
    font-family: "Oswald", sans-serif; font-weight: 500;
    font-size: 19px; line-height: 21px; color: var(--navy);
  }
  .service-icon { flex: none; width: 22px; height: 22px; margin-top: 0; }
  .tagline {
    position: absolute; left: 113px; top: 400px; width: 563px; height: 47px;
    background: var(--green); border-radius: 24px;
    font-family: "Oswald", sans-serif; font-weight: 500;
    font-size: 17px; line-height: 47px; color: var(--white);
    padding-left: 20px;
  }
  .shapes { position: absolute; left: 0; top: 0; }
</style>
</head>
<body>
<main class="display">
  <div class="photo-area" role="img" aria-label="Faded photo of two smiling colleagues working together at a laptop in a bright office"></div>

  <svg class="shapes" width="788" height="527" viewBox="0 0 788 527" aria-hidden="true">
    <circle cx="800" cy="428" r="70" fill="none" stroke="var(--navy)" stroke-width="38"/>
    <circle cx="800" cy="428" r="35" fill="var(--green)"/>
    <path d="M80 527 Q110 478 170 478 L640 478 Q690 478 706 527" fill="none" stroke="var(--green)" stroke-width="1.5"/>
    <path d="M95 527 Q112 490 160 490 L640 490 Q672 490 690 527 Z" fill="var(--navy)"/>
  </svg>

  <div class="brand">
    <span class="brand-dot"></span>
    <span class="brand-name">WORKFORCE ANCHOR PARTNERS</span>
  </div>

  <h1 class="headline">An Essential Part of Business</h1>

  <svg width="0" height="0" style="position:absolute">
    <defs>
      <g id="icon-base">
        <circle cx="11" cy="11" r="10.5" fill="var(--ring)"/>
        <circle cx="11" cy="11" r="8.5" fill="var(--navy-deep)"/>
      </g>
    </defs>
  </svg>

  <div class="service" style="left:115px;top:200px">
    <svg class="service-icon" viewBox="0 0 22 22"><use href="#icon-base"/><rect x="8" y="6.5" width="6" height="8" fill="none" stroke="#fff" stroke-width="1"/></svg>
    <span>Cafeteria/FSA/HRA Administration</span>
  </div>
  <div class="service" style="left:115px;top:238px">
    <svg class="service-icon" viewBox="0 0 22 22"><use href="#icon-base"/><circle cx="11" cy="8" r="2" fill="none" stroke="#fff"/><circle cx="8" cy="13.5" r="2" fill="none" stroke="#fff"/><circle cx="14" cy="13.5" r="2" fill="none" stroke="#fff"/></svg>
    <span>Human Resource Administration,<br>Compliance Management,<br>and Consulting</span>
  </div>
  <div class="service" style="left:115px;top:318px">
    <svg class="service-icon" viewBox="0 0 22 22"><use href="#icon-base"/><circle cx="8" cy="9" r="1.6" fill="#fff"/><circle cx="14" cy="9" r="1.6" fill="#fff"/><path d="M6 15 h10" stroke="#fff"/></svg>
    <span>Talent Acquisition</span>
  </div>
  <div class="service" style="left:115px;top:357px">
    <svg class="service-icon" viewBox="0 0 22 22"><use href="#icon-base"/><rect x="7.5" y="6" width="7" height="10" fill="none" stroke="#fff"/><path d="M9 9h4M9 11.5h4M9 14h2" stroke="#fff" stroke-width=".8"/></svg>
    <span>Onboarding</span>
  </div>

  <div class="service" style="left:460px;top:200px">
    <svg class="service-icon" viewBox="0 0 22 22"><use href="#icon-base"/><rect x="7.5" y="6" width="7" height="10" rx="1" fill="none" stroke="#fff"/><path d="M11 8v6" stroke="#fff"/></svg>
    <span>Payroll</span>
  </div>
  <div class="service" style="left:460px;top:239px">
    <svg class="service-icon" viewBox="0 0 22 22"><use href="#icon-base"/><circle cx="7.5" cy="10" r="1.6" fill="#fff"/><circle cx="11" cy="9" r="1.6" fill="#fff"/><circle cx="14.5" cy="10" r="1.6" fill="#fff"/><path d="M5.5 14.5h11" stroke="#fff"/></svg>
    <span>Benefits Management</span>
  </div>
  <div class="service" style="left:460px;top:278px">
    <svg class="service-icon" viewBox="0 0 22 22"><use href="#icon-base"/><circle cx="11" cy="11" r="5" fill="none" stroke="#fff"/><path d="M11 8v3l2 1.5" stroke="#fff" fill="none"/></svg>
    <span>Time and Attendance</span>
  </div>
  <div class="service" style="left:460px;top:317px">
    <svg class="service-icon" viewBox="0 0 22 22"><use href="#icon-base"/><circle cx="11" cy="10" r="3" fill="none" stroke="#fff"/><path d="M10 14h2v2h-2z" fill="#fff"/></svg>
    <span>Performance Management</span>
  </div>
  <div class="service" style="left:460px;top:357px">
    <svg class="service-icon" viewBox="0 0 22 22"><use href="#icon-base"/><rect x="6.5" y="8" width="9" height="6" fill="none" stroke="#fff"/><path d="M6.5 16h9" stroke="#fff"/></svg>
    <span>COBRA Administration</span>
  </div>

  <p class="tagline">Human Capital Management Solutions for the entire employee Lifecycle</p>
</main>
</body>
</html>
```